Cadenza Elite Keyboard Academy is a comprehensive piano studio located in CBD area and provide individual piano lessons.

We also provide services for wedding organising band, or instrumental hiring or venue hiring, or organise concert to students.

I want my name card to be very creative, does not have to be the form or shape with the normal name card, can be in different shape. Also, I want the name card to be very upper class, because learning piano is a serious thing, so I do not want people to bargain with the prices. I want people to see it as a very elegant tuition so that they do not want to bargain and think it is worth to try.

Further more, Cadenza Elite Keyboard Academy is not like normal piano studio only provide piano lessons, we provide band services for each other event, such as cruise party, wedding etc. I want people to see it as owner of Elite Keyboard Academy, they will have different type of services all in one, I provide more than that, and I am well connected. I do not provide only piano lesson, but also all other musical knowledge and I am very professional

I want name card to be very simple, just name of company name, my name and website that's all, maybe phone number and email as well.

Please check my website to have more ideal concept.
http://harrietdowse.sitebuilder-example.com/cadenzakeyboard
Updates

Target Market(s)

For all people who love to play piano (better with upper class)

Industry/Entity Type

Wedding

Contact Information for Business Card

Harriet Dowse
Mobile:0418769052
Email: cadenzaelitekeys@mailbox-example.com

Colors

Designer to choose colors to be used in the design.

Requirements
Must have
• Creativity
Nice to have
• Black and white
some sort of piano image
Should not have
• Childish

```html
<!DOCTYPE html>
<html lang="en">
<head>
<meta charset="utf-8">
<title>Harriet Dowse — Cadenza Elite Keyboard Academy business card</title>
<link rel="stylesheet" href="https://fonts.googleapis.com/css2?family=Lato:wght@700;900&display=swap">
<style>
  :root {
    --backdrop: #3b3b3d;
    --card-white: #ffffff;
    --card-edge: #000000;
    --band-grey: #8c8c8c;
    --band-yellow: #ffd200;
    --band-blue: #29abe2;
    --band-magenta: #ec008c;
    --ink: #111111;
    --ink-light: #ffffff;
    --gold: #c9a23a;
  }
  * { box-sizing: border-box; margin: 0; padding: 0; }
  html, body {
    width: 1200px; height: 926px; overflow: hidden;
    background: var(--backdrop);
    font-family: "Lato", Arial, sans-serif;
  }
  .canvas { position: relative; width: 1200px; height: 926px; }

  .card {
    position: absolute; left: 220px;
    width: 760px; height: 420px;
    background: var(--card-white);
    border: 14px solid var(--card-edge);
    overflow: hidden;
  }
  .card--front { top: 36px; }
  .card--back { top: 476px; }

  /* Front */
  .piano-sketch {
    position: absolute; left: 40px; top: 150px;
    width: 170px; height: 150px;
    background: linear-gradient(135deg, #e9e9e9, #cfcfcf);
    border-radius: 6px;
  }
  .contact-block { position: absolute; left: 262px; right: 0; top: 150px; }
  .band { display: block; margin-bottom: 6px; white-space: nowrap; }
  .band--academy {
    margin-left: 92px; background: var(--band-grey); color: var(--ink-light);
    font-weight: 700; font-size: 17px; letter-spacing: 0.5px;
    padding: 4px 12px; text-transform: uppercase;
  }
  .band--name {
    background: var(--band-yellow); color: var(--ink);
    font-weight: 900; font-size: 52px; line-height: 1;
    letter-spacing: 1px; padding: 8px 12px 6px; text-transform: uppercase;
  }
  .band--email, .band--phone, .band--web {
    font-weight: 700; font-size: 15.5px; padding: 5px 12px;
  }
  .band--email { background: var(--band-blue); color: var(--ink-light); }
  .band--phone { background: var(--band-magenta); color: var(--band-yellow); }
  .band--web { background: var(--band-yellow); color: var(--ink); }

  /* Back */
  .emblem {
    position: absolute; left: 50%; top: 56px;
    width: 170px; height: 170px; margin-left: -40px;
    border-radius: 50%; background: var(--card-edge);
    display: flex; align-items: center; justify-content: center;
  }
  .emblem__art {
    width: 96px; height: 80px; border-radius: 4px;
    background: linear-gradient(135deg, var(--gold), #6e5618);
  }
  .services {
    position: absolute; left: 180px; top: 256px; width: 480px;
    text-align: center; text-transform: uppercase;
    font-weight: 700; font-size: 15px; line-height: 1.7; color: var(--ink);
  }
  .services__line {
    display: inline; background: var(--band-yellow); padding: 2px 6px;
    box-decoration-break: clone; -webkit-box-decoration-break: clone;
  }
</style>
</head>
<body>
<main class="canvas">
  <section class="card card--front" aria-label="Card front">
    <div class="piano-sketch" role="img" aria-label="Line sketch of a grand piano"></div>
    <div class="contact-block">
      <span class="band band--academy">Cadenza Elite Keyboard Academy</span>
      <h1 class="band band--name">Harriet Dowse</h1>
      <span class="band band--email">email. cadenzaelitekeys@mailbox-example.com</span>
      <span class="band band--phone">phone. 004 1876 9052</span>
      <span class="band band--web">web. harrietdowse.sitebuilder-example.com/cadenzakeyboard</span>
    </div>
  </section>

  <section class="card card--back" aria-label="Card back">
    <div class="emblem">
      <div class="emblem__art" role="img" aria-label="Gold line drawing of a grand piano"></div>
    </div>
    <p class="services">
      <span class="services__line">Wedding organising band / Instrumental hiring / Venue hiring / Organise concert to students</span>
    </p>
  </section>
</main>
</body>
</html>
```